Occupational Therapist does home accessibility for disabled folks; needs business card design

We need a business card for a company in Portland, Oregon that specializes in making homes accessible, comfortable, and functional for people who are disabled or aging who would like to stay in THEIR home. Our medical background as Occupational Therapists allows us to translate the functional needs of the person into the recommendations for the design of the home remodel.

Target Market(s)

Elderly, children of elderly
People with disabilities, families of people with disabilities

Industry/Entity Type

Business

Contact Information for Business Card

Company name: HomeWise
Name: Danielle Reyes Crawford, OTR/L, CAPS, ECHM
Occupational Therapist, Home Modification & Accessibility Specialist
website: www.homewiseforyears.com
email: homewiseforyears@nestmail.example
phone: (503)218-4057
CCB #: 487315

Font styles to use
Sans Serif

Requirements
Must have
• My logo
• Easy to read font with contrasting background
• Please list the Services offered: Occupational Therapy, Home safety & accessibility assessments, Home modification consulting, project management
Nice to have
• Friendly, welcoming feel
Should not have
• Dark colored background

```html
<!DOCTYPE html>
<html lang="en">
<head>
<meta charset="utf-8">
<title>HomeWise Business Card</title>
<link rel="stylesheet" href="https://fonts.googleapis.com/css2?family=Source+Sans+3:wght@300;400;600;700&display=swap">
<style>
  :root {
    --stage: #3b3431;
    --card-white: #fbfbf9;
    --brand-orange: #d0811d;
    --ink: #3a3a3a;
    --ink-soft: #555555;
    --on-orange: #ffffff;
  }
  * { box-sizing: border-box; margin: 0; padding: 0; }
  html, body {
    width: 1200px;
    height: 844px;
    overflow: hidden;
    background: var(--stage);
    font-family: "Source Sans 3", "Myriad Pro", Arial, sans-serif;
  }
  .stage {
    position: relative;
    width: 1200px;
    height: 844px;
    display: flex;
    align-items: center;
    justify-content: center;
    gap: 50px;
  }
  .card {
    position: relative;
    width: 530px;
    height: 303px;
    border-radius: 2px;
    box-shadow: 0 10px 28px rgba(0,0,0,0.45);
  }
  /* Front */
  .card-front { background: var(--card-white); color: var(--ink); }
  .brand {
    position: absolute;
    top: 34px;
    right: 32px;
    display: flex;
    align-items: center;
    gap: 10px;
  }
  .brand-square {
    width: 22px;
    height: 22px;
    background: var(--brand-orange);
  }
  .brand-name {
    font-size: 40px;
    font-weight: 600;
    color: var(--brand-orange);
    letter-spacing: 0.5px;
    line-height: 1;
  }
  .licence {
    position: absolute;
    top: 112px;
    left: 30px;
    font-size: 19px;
    color: var(--ink-soft);
  }
  .licence-label { color: var(--brand-orange); }
  .identity {
    position: absolute;
    left: 30px;
    top: 168px;
  }
  .person-name {
    font-size: 19px;
    font-weight: 700;
    color: var(--brand-orange);
  }
  .credentials {
    font-size: 12px;
    font-weight: 400;
    color: var(--brand-orange);
  }
  .role {
    margin-top: 4px;
    font-size: 14px;
    line-height: 1.25;
    color: var(--ink);
  }
  .contact {
    position: absolute;
    left: 30px;
    right: 24px;
    bottom: 26px;
    display: flex;
    gap: 12px;
    font-size: 12.5px;
    color: var(--ink);
    white-space: nowrap;
  }
  .contact-label { color: var(--brand-orange); font-weight: 700; }
  .contact-web { color: var(--brand-orange); font-weight: 600; }
  /* Back */
  .card-back {
    background: var(--brand-orange);
    color: var(--on-orange);
    display: flex;
    flex-direction: column;
    align-items: center;
    justify-content: center;
    text-align: center;
  }
  .services-title {
    font-size: 19px;
    font-weight: 700;
    letter-spacing: 0.3px;
    margin-bottom: 14px;
  }
  .services-list { list-style: none; }
  .services-list li {
    font-size: 17px;
    font-weight: 300;
    line-height: 1.35;
  }
</style>
</head>
<body>
  <main class="stage">
    <section class="card card-front" aria-label="Business card front">
      <div class="brand">
        <span class="brand-square" aria-hidden="true"></span>
        <span class="brand-name">HomeWise</span>
      </div>
      <p class="licence"><span class="licence-label">CCB #:</span> 487315</p>
      <div class="identity">
        <p class="person-name">Danielle Reyes Crawford,<span class="credentials">OTR/L, CAPS, ECHM</span></p>
        <p class="role">Occupational Therapist,<br>Home Modification &amp; Accessibility Specialist</p>
      </div>
      <p class="contact">
        <span><span class="contact-label">P:</span> (503)218-4057</span>
        <span><span class="contact-label">E:</span> homewiseforyears@nestmail.example</span>
        <span class="contact-web">www.homewiseforyears.com</span>
      </p>
    </section>

    <section class="card card-back" aria-label="Business card back">
      <h2 class="services-title">SERVICES OFFERED</h2>
      <ul class="services-list">
        <li>Occupational Therapy</li>
        <li>Home Safety &amp; Accessibility Assessments</li>
        <li>Home Modification Consulting</li>
        <li>Project Management</li>
      </ul>
    </section>
  </main>
</body>
</html>
```